Bref créative
Corvel Byte - PC Service Company
Business Card, Stationery, Envelope
Professional
Wade Harlock, MCP
4710 Pelham Ferry Rd.
Gainesville, GA 30548
wtharlock@corvelbyte.example
www.corvelbyte.example
Stationery:
Stationery should be letter size (8.5W x 11H). I think the header should be logo + graphics only and all other info should be in the footer but I am flexable. The design should include:
- My address
- My (770) 555-0148
- My URL
Use either logo, use only the colors found in the logo. The font should be Century Gothic or similar.
Envelope:
The envelope should be #10 size (4 1/8H x 9 1/2W). The envelope should use the logo with the transparent background and should include our address as the return address in the upper left corner. The envelope design should be very simple and should match the stationery. The font used should be Century Gothic or similar.
Business Card:
The front of the card should have a white background and should contain all of the following:
- My name and title
- My (770) 555-0172
- My email address
Optional info for the front of the card if you can display it in an attractive way without making the card appear too cluttered:
- My Address
Please note my URL must be on one side of the card, it can be the front or the back.
The font used in our logo is Century Gothic. I can provide our logo in additional formats if needed, just leave a request for the format you need.
Use only the colors found in the logo plus white and black. I want the card to look professional, clean and high-tech.
Please be sure to read my comments as the contest progresses as I may have additional requests once I start seeing some designs.
The back of the card should be in one of the following formats:
1. Only our URL: www.corvelbyte.example
2. Our URL and our Logo
3. Only our logo
Please choose the option you feel is most attractive. If you do not use the URL on the back of the card you must use it on the front.
The back of the card should be white, blue or the same grey seen in CorvelFinalDark.png and may include some minimal graphics in addition to the logo (if used).

```html
<!DOCTYPE html>
<html lang="en">
<head>
<meta charset="utf-8">
<title>Corvel Byte – Stationery Set</title>
<link href="https://fonts.googleapis.com/css2?family=Questrial&display=swap" rel="stylesheet">
<style>
  :root{
    --backdrop:#4b5051;
    --paper:#ffffff;
    --brand-green:#7fb539;
    --brand-blue:#2a5d8f;
    --ink:#3c4144;
    --ink-soft:#6b7073;
  }
  *{margin:0;padding:0;box-sizing:border-box}
  html,body{width:1200px;height:1104px;overflow:hidden}
  body{background:var(--backdrop);font-family:"Questrial",sans-serif;color:var(--ink);position:relative}

  .brand{display:flex;align-items:center;gap:8px;font-family:"Questrial",sans-serif;color:var(--ink);letter-spacing:-.5px;white-space:nowrap}
  .brand-dot{border-radius:50%;background:var(--brand-green);flex:none}

  /* business card front */
  .card-front{position:absolute;left:120px;top:96px;width:345px;height:264px;background:var(--paper);box-shadow:0 2px 6px rgba(0,0,0,.35)}
  .card-front .brand{position:absolute;left:12px;top:14px;font-size:32px}
  .card-front .brand-dot{width:40px;height:40px}
  .card-holder{position:absolute;left:24px;top:196px}
  .card-holder .name{color:var(--brand-blue);font-size:15px;font-weight:bold}
  .card-holder .title{color:var(--brand-green);font-size:9px;text-align:right;margin-top:2px}
  .card-contact{position:absolute;left:150px;top:196px;font-size:8.5px;line-height:12px;color:var(--ink-soft)}
  .card-front .edge{position:absolute;left:0;right:0;bottom:0;height:5px;background:var(--brand-green)}

  /* business card back */
  .card-back{position:absolute;left:120px;top:384px;width:345px;height:252px;background:var(--brand-green);box-shadow:0 2px 6px rgba(0,0,0,.35)}
  .card-back .brand{position:absolute;left:50%;top:92px;transform:translateX(-50%);font-size:36px;color:#fff}
  .card-back .brand-dot{width:42px;height:42px;background:#fff}
  .card-back .url{position:absolute;left:0;right:0;top:146px;text-align:center;color:#fff;font-size:10px;letter-spacing:.5px}

  /* letterhead */
  .letterhead{position:absolute;left:510px;top:90px;width:654px;height:915px;background:var(--paper);box-shadow:0 2px 8px rgba(0,0,0,.35)}
  .letterhead .brand{position:absolute;left:14px;top:16px;font-size:34px}
  .letterhead .brand-dot{width:44px;height:44px}
  .letter-address{position:absolute;right:42px;top:12px;font-size:8px;line-height:11px;color:var(--ink-soft)}
  .letter-bar{position:absolute;right:10px;top:10px;width:16px;height:52px;background:var(--brand-green)}
  .letter-body{position:absolute;left:46px;top:140px;width:580px}
  .letter-body h1{font-size:18px;font-weight:normal;color:var(--ink);margin-bottom:10px}
  .letter-body p{font-size:11.6px;line-height:14.4px;color:var(--ink);text-align:justify}

  /* envelope */
  .envelope{position:absolute;left:495px;top:636px;width:585px;height:318px;background:var(--paper);box-shadow:3px 6px 14px rgba(0,0,0,.45)}
  .envelope .brand{position:absolute;left:20px;top:16px;font-size:27px}
  .envelope .brand-dot{width:34px;height:34px}
  .return-address{position:absolute;left:66px;top:62px;font-size:8px;line-height:11px;color:var(--ink-soft)}
  .envelope .edge{position:absolute;left:0;right:0;bottom:0;height:5px;background:var(--brand-green)}
</style>
</head>
<body>

<section class="card-front">
  <div class="brand"><span class="brand-dot"></span>corvelbyte</div>
  <div class="card-holder">
    <div class="name">Wade Harlock</div>
    <div class="title">MCP</div>
  </div>
  <div class="card-contact">
    4710 Pelham Ferry Rd.<br>
    Gainesville, GA 30548<br>
    P (770) 555-0148<br>
    C (770) 555-0172<br>
    wtharlock@corvelbyte.example
  </div>
  <div class="edge"></div>
</section>

<section class="card-back">
  <div class="brand"><span class="brand-dot"></span>corvelbyte</div>
  <div class="url">www.corvelbyte.example</div>
</section>

<section class="letterhead">
  <div class="brand"><span class="brand-dot"></span>corvelbyte</div>
  <div class="letter-address">
    4710 Pelham Ferry Rd.<br>
    Gainesville, GA 30548<br>
    (770) 555-0148<br>
    www.corvelbyte.example<br>
    wtharlock@corvelbyte.example
  </div>
  <div class="letter-bar"></div>
  <div class="letter-body">
    <h1>including versions of Lorem Ipsum</h1>
    <p>Lorem Ipsum is simply dummy text of the printing and typesetting industry. Lorem Ipsum has been the industry's standard dummy text ever since the 1500s, when an unknown printer took a galley of type and scrambled it to make a type specimen book. It has survived not only five centuries, but also the leap into electronic typesetting, remaining essentially unchanged. It was popularised in the 1960s with the release of Letraset sheets containing Lorem Ipsum passages, and more recently with desktop publishing software like Aldus PageMaker including versions of Lorem Ipsum. Lorem Ipsum is simply dummy text of the printing and typesetting industry. Lorem Ipsum has been the industry's standard dummy text ever since the 1500s, when an unknown printer took a galley of type and scrambled it to make a type specimen book. It has survived not only five centuries, but also the leap into electronic typesetting, remaining essentially unchanged. It was popularised in the 1960s with the release of Letraset sheets containing Lorem Ipsum passages, and more recently with desktop publishing software like Aldus PageMaker including versions of Lorem Ipsum. Lorem Ipsum is simply dummy text of the printing and typesetting industry. Lorem Ipsum has been the industry's standard dummy text ever since the 1500s, when an unknown printer took a galley of type and scrambled it to make a type specimen book, and more recently with desktop publishing software like Aldus PageMaker including versions of Lorem Ipsum.</p>
  </div>
</section>

<section class="envelope">
  <div class="brand"><span class="brand-dot"></span>corvelbyte</div>
  <div class="return-address">
    4710 Pelham Ferry Rd.<br>
    Gainesville, GA 30548
  </div>
  <div class="edge"></div>
</section>

</body>
</html>
```